Dribblecake Bites
2 x business cards, letter head, with complements and envelopes
Dribblecake Bites - Food
Creative Brief
Bright & Fun-filled
Percy Lantern
Managing Director
NA
Percy.Lantern@dribblecakebites.com.au
www.dribblecakebites.com.au
card 2 Teodor Blum Business Manager 0417583926 Teodorblum@quillnet.com www.dribblecakebites.com.au
logo ect

```html
<!DOCTYPE html>
<html lang="en">
<head>
<meta charset="utf-8">
<title>Dribblecake Bites – Business Card</title>
<link rel="stylesheet" href="https://fonts.googleapis.com/css2?family=PT+Sans:ital,wght@0,400;0,700;1,700&display=swap">
<style>
  :root {
    --backdrop: #e4e0db;
    --card-white: #ffffff;
    --choc-dark: #3e1708;
    --choc: #5a2610;
    --choc-mid: #8e4a24;
    --choc-light: #7a3a1a;
    --caramel: #c9621c;
    --ink: #3b2a22;
    --cream: #f1e2d3;
    --blush: #e8d6c8;
  }
  * { box-sizing: border-box; margin: 0; padding: 0; }
  html, body {
    width: 1200px; height: 852px; overflow: hidden;
    background: var(--backdrop);
    font-family: "PT Sans", sans-serif;
  }
  .stage {
    width: 1200px; height: 852px;
    display: flex; align-items: center; justify-content: center; gap: 44px;
  }
  .card {
    position: relative; width: 540px; height: 309px;
    border-radius: 18px; overflow: hidden;
    box-shadow: 0 10px 26px rgba(40, 20, 10, 0.25);
  }

  /* Front */
  .card--front { background: var(--card-white); }
  .brand {
    position: absolute; top: 44px; left: 0; right: 0; text-align: center;
  }
  .brand__name {
    font-weight: 700; font-size: 50px; line-height: 1; color: var(--choc);
  }
  .brand__tagline {
    margin-top: 6px; font-weight: 700; font-size: 14px; color: var(--caramel);
  }
  .band-top {
    position: absolute; top: 132px; left: 0; right: 0; height: 14px;
    background: var(--choc-light);
    border-top: 3px solid var(--choc-dark);
  }
  .name-band {
    position: absolute; top: 146px; left: 0; right: 0; height: 50px;
    background: var(--choc);
    display: flex; align-items: center; justify-content: center; gap: 10px;
    color: var(--card-white);
  }
  .name-band__name { font-weight: 700; font-size: 19px; }
  .name-band__sep { font-size: 19px; opacity: 0.85; }
  .name-band__role { font-size: 15px; }
  .contact {
    position: absolute; top: 220px; left: 0; right: 0;
    text-align: center; font-size: 14px; line-height: 1.8; color: var(--ink);
  }
  .contact__label { font-weight: 700; font-style: italic; color: var(--choc); }
  .contact__item { margin: 0 6px; }

  /* Back */
  .card--back {
    background: radial-gradient(ellipse at 50% 40%, var(--choc-mid) 0%, var(--choc) 55%, var(--choc-dark) 100%);
  }
  .mascot-area {
    position: absolute; top: 70px; left: 50%; width: 120px; height: 120px;
    margin-left: -60px; border-radius: 50%;
    background: radial-gradient(circle at 45% 40%, var(--choc-light), var(--choc-dark));
  }
  .back-web {
    position: absolute; bottom: 66px; left: 0; right: 0; text-align: center;
    font-size: 16px; color: var(--blush); letter-spacing: 0.3px;
  }
</style>
</head>
<body>
<main class="stage">
  <section class="card card--front" aria-label="Business card front">
    <header class="brand">
      <div class="brand__name">Dribblecake Bites</div>
      <div class="brand__tagline">The Yummy Mini Dutch Pancakes</div>
    </header>
    <div class="band-top"></div>
    <div class="name-band">
      <span class="name-band__name">Percy Lantern</span>
      <span class="name-band__sep">/</span>
      <span class="name-band__role">Managing Director</span>
    </div>
    <div class="contact">
      <div>
        <span class="contact__item"><span class="contact__label">Phone:</span> 0438261947</span>
        <span class="contact__item"><span class="contact__label">Email:</span> Percy.Lantern@dribblecakebites.com.au</span>
      </div>
      <div><span class="contact__label">Web:</span> www.dribblecakebites.com.au</div>
    </div>
  </section>

  <section class="card card--back" aria-label="Business card back">
    <div class="mascot-area" role="img" aria-label="Smiling pancake mascot illustration"></div>
    <div class="back-web">www.dribblecakebites.com.au</div>
  </section>
</main>
</body>
</html>
```